Help this startup build its beautiful website

We are an online payment service provider startup looking for a modern, beautiful with great user experience web design.

You can use the big companies as a reference like, TillWave, Brindle, Plinth,
We need a design for our wordpress website.

It doesn't need to have the same look and feel of the presentation

Font styles to use
Serif
Sans Serif

Colors

Designer to choose colors to be used in the design.

```html
<!DOCTYPE html>
<html lang="en">
<head>
<meta charset="utf-8">
<title>Payvanta — Online payment service provider</title>
<link href="https://fonts.googleapis.com/css2?family=Montserrat:wght@400;500;600&family=Roboto:wght@300;400;500&display=swap" rel="stylesheet">
<style>
:root{
  --navy:#0e3c7a;
  --royal:#1560b4;
  --sky:#9cc3e6;
  --orange:#fd8115;
  --orange-glow:rgba(253,90,40,.45);
  --ink:#1d1d1d;
  --body:#444;
  --mist:#f6f6f6;
  --line:#e6e6e6;
  --link-blue:#1a5fb4;
}
*{margin:0;padding:0;box-sizing:border-box}
html,body{width:1200px;height:2709px;overflow:hidden;background:#fff}
body{position:relative;font-family:"Roboto",sans-serif;color:var(--body)}
.abs{position:absolute}
.decor{position:absolute;left:0;top:0}
h1,h2,h3{font-family:"Montserrat",sans-serif;color:var(--ink);font-weight:500}
.btn{position:absolute;display:flex;align-items:center;justify-content:center;background:var(--orange);color:#fff;font-family:"Roboto",sans-serif;font-weight:500;border-radius:24px;box-shadow:0 10px 18px -6px var(--orange-glow)}
.art{position:absolute;border-radius:6px}

/* header */
.brand{left:112px;top:34px;display:flex;align-items:center;gap:12px;color:#fff;font-family:"Montserrat",sans-serif;font-size:36px;font-weight:500}
.brand-mark{width:44px;height:44px;background:#fff;border-radius:6px}
.nav{left:0;top:52px;font-size:16px;font-weight:500}
.nav a{position:absolute;white-space:nowrap;text-decoration:none}
.nav .light{color:#fff}
.nav .dark{color:var(--ink)}

/* hero */
.hero-title{left:598px;top:232px;font-size:44px}
.hero-sub{left:597px;top:290px;font-size:21px;font-weight:300;color:#222}

/* services */
.section-title{left:0;width:1200px;text-align:center}
.card{position:absolute;top:742px;width:235px;height:268px;background:#fff;box-shadow:0 2px 12px rgba(0,0,0,.08);text-align:center;padding:8px 12px 0}
.card .icon{width:117px;height:117px;border-radius:50%;margin:0 auto 18px}
.card h3{font-size:16px;font-weight:500;line-height:23px;margin-bottom:5px}
.card p{font-size:14px;line-height:22px;color:#444}

/* about */
.lead{left:0;width:1200px;text-align:center;top:1156px;font-size:17px;color:var(--link-blue)}
.about-copy{left:180px;width:840px;top:1214px;text-align:center;font-size:14px;line-height:27px;color:#333}

.feature h3{font-size:22px;font-weight:500;position:absolute}
.feature p{position:absolute;font-size:14.5px;line-height:27px;color:#444}

/* newsletter */
.field{left:711px;top:2318px;width:350px;height:46px;border:1px solid #cfcfcf;background:#fff;display:flex;align-items:center;justify-content:center;font-size:13px;color:#555}
.subscribe{left:711px;top:2378px;width:350px;height:46px;background:var(--orange);color:#fff;font-size:14px;font-weight:500;display:flex;align-items:center;justify-content:center;letter-spacing:.5px}

/* footer */
.social{position:absolute;top:2547px;width:42px;height:42px;border:1px solid #d7d7d7;border-radius:50%;background:#fff}
.social::after{content:"";position:absolute;left:15px;top:15px;width:12px;height:12px;border-radius:50%;background:var(--orange)}
.foot-links{left:139px;top:2610px;font-size:14px;color:#333;display:flex;gap:24px}
.foot-mail{left:140px;top:2642px;font-size:13px;color:var(--link-blue);text-decoration:underline}
.copyright{left:753px;top:2660px;font-size:12px;color:#fff}
</style>
</head>
<body>

<svg class="decor" width="1200" height="2709" viewBox="0 0 1200 2709" aria-hidden="true">
  <g fill="var(--mist)">
    <circle cx="747" cy="142" r="29"/>
    <circle cx="1165" cy="90" r="70"/>
    <circle cx="1220" cy="365" r="55"/>
    <path d="M1200 440 C1020 460 930 560 880 720 L1200 760Z"/>
    <circle cx="5" cy="935" r="38"/>
    <circle cx="365" cy="1018" r="52"/>
    <circle cx="42" cy="1224" r="40"/>
    <path d="M660 1000 C640 1100 470 1200 480 1380 C500 1560 700 1610 820 1560 C960 1500 1010 1360 1200 1340 L1200 1000Z"/>
    <path d="M0 1440 C120 1420 220 1500 260 1600 L0 1640Z"/>
    <circle cx="1200" cy="1535" r="38"/>
    <path d="M990 1860 C1060 1830 1140 1840 1200 1880 L1200 2200 C1110 2220 1010 2180 990 2100Z"/>
    <circle cx="270" cy="2255" r="50"/>
    <circle cx="90" cy="2300" r="52"/>
  </g>
  <path d="M0 0 H700 C740 100 660 200 520 240 C380 280 390 330 520 380 C640 430 580 590 330 615 C180 630 60 600 0 560Z" fill="var(--sky)"/>
  <path d="M0 0 H680 C700 80 640 180 500 230 C360 280 370 320 500 370 C610 420 560 580 320 600 C170 610 60 580 0 540Z" fill="var(--navy)"/>
  <path d="M1200 2450 C1160 2330 1090 2260 1010 2270 C930 2280 880 2420 760 2480 C640 2530 560 2570 590 2640 C605 2680 640 2700 650 2709 H1200Z" fill="var(--royal)"/>
  <line x1="0" y1="2478" x2="1200" y2="2478" stroke="var(--line)"/>
</svg>

<div class="abs brand"><span class="brand-mark"></span>Payvanta</div>
<nav class="abs nav">
  <a class="light" style="left:372px">Home</a>
  <a class="light" style="left:483px">About us</a>
  <a class="light" style="left:613px">Services</a>
  <a class="dark" style="left:730px">FAQ</a>
  <a class="dark" style="left:813px">Contact us</a>
</nav>
<div class="btn" style="left:920px;top:40px;width:167px;height:41px;font-size:16px">Request A Demo</div>

<div class="art" role="img" aria-label="Isometric illustration of a phone with a credit card, pay now button and receipt" style="left:85px;top:110px;width:270px;height:390px;background:linear-gradient(150deg,#2a7fd8,#133e8e 60%,#0a2b66)"></div>
<h1 class="abs hero-title">Welcome to Payvanta</h1>
<p class="abs hero-sub">Lorem ipsum dolor sit amet, consectetur adipiscing elit</p>
<div class="btn" style="left:600px;top:358px;width:182px;height:48px;font-size:18px">Get Started</div>

<h2 class="abs section-title" style="top:660px;font-size:44px">Services</h2>
<div class="card" style="left:112px">
  <div class="icon" role="img" aria-label="E-commerce illustration" style="background:radial-gradient(circle at 40% 40%,#7a4a66,#3c1230)"></div>
  <h3>E-COMMERCE</h3>
  <p>Start accepting online payments on your mobile app, e-commerce website or physical device.</p>
</div>
<div class="card" style="left:360px">
  <div class="icon" role="img" aria-label="Smart billing illustration" style="background:radial-gradient(circle at 40% 40%,#3aa9a0,#0f6e6b)"></div>
  <h3 style="margin-top:-2px">SMART BILLING</h3>
  <p>You can collect your subscription payments in a very efficient and automated way with our recurring billing system</p>
</div>
<div class="card" style="left:607px">
  <div class="icon" role="img" aria-label="Payment link illustration" style="background:radial-gradient(circle at 40% 40%,#d6238f,#8a0c5e)"></div>
  <h3>PAYMENT LINK</h3>
  <p>Just send the link by email, ChatLoop or any other messenger and receive that payment instantly.</p>
</div>
<div class="card" style="left:854px">
  <div class="icon" role="img" aria-label="Developer API illustration" style="background:#0c1f33"></div>
  <h3>EASY ON<br>DEVELOPERS</h3>
  <p>API in 30 seconds implementation guaranteed!</p>
</div>

<h2 class="abs section-title" style="top:1120px;font-size:30px">Payvanta</h2>
<p class="abs lead">Online payment service provider</p>
<p class="abs about-copy">Lorem ipsum dolor sit amet, consectetur adipiscing elit, sed do eiusmod tempor incididunt ut labore et dolore magna aliqua. Ut enim ad minim veniam, quis nostrud exercitation ullamco laboris nisi ut aliquip ex ea commodo consequat. Duis aute irure dolor in reprehenderit in voluptate velit esse cillum dolore eu fugiat nulla pariatur</p>
<div class="btn" style="left:527px;top:1335px;width:145px;height:41px;font-size:16px">Read More</div>

<h2 class="abs section-title" style="top:1482px;font-size:32px">No more chargebacks!</h2>
<section class="feature">
  <div class="art" role="img" aria-label="Illustration of a security shield connected to servers" style="left:138px;top:1595px;width:332px;height:220px;background:radial-gradient(ellipse at 50% 45%,#dfe6ff,#f6f7ff 70%)"></div>
  <h3 style="left:582px;top:1584px">SECURITY GUARANTEED</h3>
  <p style="left:582px;top:1629px;width:480px">As a PCI compliant we strictly implement the most reliable algorithms, technology and processes to handle,guard and save every piece of sensible data like personal and payment information y our server infræstructure.</p>
  <div class="btn" style="left:582px;top:1774px;width:151px;height:44px;font-size:17px">Read More</div>
</section>
<section class="feature">
  <h3 style="left:110px;top:1918px">BANK NETWORK</h3>
  <p style="left:110px;top:1963px;width:480px">Working as an agregator and sevice provider we have partnered with some local and international banks that allow us to provide the best prices on the market and as a support and liability for our customers.</p>
  <div class="btn" style="left:110px;top:2108px;width:151px;height:44px;font-size:17px">Read More</div>
  <div class="art" role="img" aria-label="Isometric illustration of two people analysing charts on a large screen" style="left:660px;top:1860px;width:428px;height:290px;background:radial-gradient(ellipse at 55% 50%,#c9d8f7,#f2f5fc 70%,#fff)"></div>
</section>

<h2 class="abs" style="left:139px;top:2315px;font-size:32px">Get more Information</h2>
<p class="abs" style="left:140px;top:2364px;width:470px;font-size:14px;line-height:28px">Sed ut perspiciatis unde omnis iste natus error sit voluptatem accusantium doloremque laudantium, totam rem aperiam</p>
<div class="abs field">Enter Your Email</div>
<div class="abs subscribe">SUBSCRIBE NOW</div>

<span class="social" style="left:141px"></span>
<span class="social" style="left:197px"></span>
<span class="social" style="left:254px"></span>
<span class="social" style="left:309px"></span>
<span class="social" style="left:366px"></span>
<div class="abs foot-links"><span>Home</span><span>About us</span><span>Services</span><span>FAQ</span><span>Contact us</span></div>
<a class="abs foot-mail">hello@payvanta.example</a>
<p class="abs copyright">Copyright.the Company Name.2019 | All Rights Reserved</p>

</body>
</html>
```